professional business card

A Clean looking business card for a money transfer company. Our company is call Velorix= Transfer + Send = Transcend (next level)
to show professionalism as well as some effects to show digital tech.

1 side to have position, name and address
2 side to have company name and show that we provide money exchange and cross-border money transfer

Target Market(s)

Remittance companies and high net worth individuals

Industry/Entity Type

Finance

Contact Information for Business Card

Name, address, email, title, services- money exchange and cross-border remittance

Requirements
Nice to have
• Digital age feel

```html
<!DOCTYPE html>
<html lang="en">
<head>
<meta charset="utf-8">
<title>Velorix business card</title>
<link href="https://fonts.googleapis.com/css2?family=Montserrat:wght@400;500;600;700&display=swap" rel="stylesheet">
<style>
  :root {
    --bg: #d9d9d9;
    --navy: #263545;
    --navy-soft: #2c3c4d;
    --cyan: #6fcbda;
    --white: #ffffff;
    --ink: #1f2c3a;
  }
  * { box-sizing: border-box; margin: 0; padding: 0; }
  html, body { width: 1200px; height: 802px; overflow: hidden; }
  body {
    background: var(--bg);
    font-family: "Montserrat", Arial, sans-serif;
    display: flex;
    align-items: center;
    justify-content: center;
    gap: 40px;
  }
  .card {
    position: relative;
    width: 560px;
    height: 320px;
    border-radius: 22px;
    overflow: hidden;
    box-shadow: 0 10px 28px rgba(0,0,0,0.22);
  }

  /* Front side */
  .card-front { background: var(--white); }
  .front-band {
    position: absolute; left: 0; top: 112px;
    width: 100%; height: 150px;
    background: var(--navy);
  }
  .front-accent {
    position: absolute; right: 0; top: 28px;
    width: 170px; height: 84px;
    background: var(--cyan);
  }
  .brand {
    position: absolute;
    display: flex; align-items: center; gap: 14px;
  }
  .brand-dot { width: 22px; height: 22px; background: var(--cyan); }
  .brand-name {
    font-weight: 500; letter-spacing: 3px; text-transform: uppercase;
  }
  .card-front .brand { left: 34px; top: 40px; }
  .card-front .brand-name { font-size: 40px; color: var(--ink); }
  .person { position: absolute; left: 34px; top: 128px; color: var(--white); }
  .person-name { font-size: 22px; font-weight: 700; color: var(--cyan); }
  .person-title { font-size: 14px; font-weight: 400; margin-top: 2px; }
  .contact-list { list-style: none; margin-top: 10px; }
  .contact-list li {
    display: flex; align-items: center; gap: 8px;
    font-size: 14px; line-height: 22px;
  }
  .contact-list svg { width: 12px; height: 12px; fill: var(--cyan); }
  .address {
    position: absolute; left: 34px; bottom: 20px;
    font-size: 14px; color: var(--ink); letter-spacing: 0.3px;
  }

  /* Back side */
  .card-back { background: var(--navy); }
  .back-pattern { position: absolute; inset: 0; background: var(--navy-soft); opacity: 0.6; }
  .card-back .brand { left: 150px; top: 110px; }
  .card-back .brand-name { font-size: 42px; color: var(--white); }
  .tagline {
    position: absolute; left: 0; right: 0; top: 200px;
    text-align: center;
    font-size: 15px; font-weight: 600; color: var(--white);
    letter-spacing: 0.6px;
  }
  .tagline .highlight { color: var(--cyan); }
</style>
</head>
<body>
  <section class="card card-front" aria-label="Front of business card">
    <div class="front-accent"></div>
    <div class="front-band"></div>
    <div class="brand">
      <span class="brand-dot"></span>
      <span class="brand-name">Velorix</span>
    </div>
    <div class="person">
      <p class="person-name">Dana Whitlock</p>
      <p class="person-title">CEO/Founder</p>
      <ul class="contact-list">
        <li>
          <svg viewBox="0 0 24 24" aria-hidden="true"><path d="M6.6 10.8a15.1 15.1 0 0 0 6.6 6.6l2.2-2.2a1 1 0 0 1 1-.25 11.4 11.4 0 0 0 3.6.57 1 1 0 0 1 1 1V20a1 1 0 0 1-1 1A17 17 0 0 1 3 4a1 1 0 0 1 1-1h3.5a1 1 0 0 1 1 1c0 1.25.2 2.45.57 3.57a1 1 0 0 1-.25 1z"/></svg>
          555.018.2047
        </li>
        <li>
          <svg viewBox="0 0 24 24" aria-hidden="true"><path d="M2 5h20v14H2z M2 5l10 8 10-8" /></svg>
          info@velorix.com
        </li>
        <li>
          <svg viewBox="0 0 24 24" aria-hidden="true"><circle cx="12" cy="12" r="10"/></svg>
          www.velorix.com
        </li>
      </ul>
    </div>
    <p class="address">P.O Box 7310 Harbor Lane Northvale AB 6120</p>
  </section>

  <section class="card card-back" aria-label="Back of business card">
    <div class="back-pattern" role="img" aria-label="Faint repeating pattern of brand marks across the card"></div>
    <div class="brand">
      <span class="brand-dot"></span>
      <span class="brand-name">Velorix</span>
    </div>
    <p class="tagline">we provide money <span class="highlight">exchange and cross-border</span> money transfer</p>
  </section>
</body>
</html>
```